Pillar Orchard
Professional
Mira Castellan, MBA
mira@pillarorchard.ca
www.pillarorchard.ca
Landscape layout. Please include tagline: "Building Momentum for Success"
Whatever you think will look good.

```html
<!DOCTYPE html>
<html lang="en">
<head>
<meta charset="utf-8">
<title>Pillar Orchard – Business Cards</title>
<link href="https://fonts.googleapis.com/css2?family=Open+Sans:wght@400;600;700;800&display=swap" rel="stylesheet">
<style>
  :root {
    --page-bg: #e9e6e1;
    --navy-deep: #0b1640;
    --navy: #1d3a8f;
    --navy-light: #3a63c7;
    --steel: #9aa3b0;
    --card-dark-top: #232323;
    --card-dark-bottom: #050505;
    --card-light: #ffffff;
    --text-light: #d8dbe2;
    --text-dark: #3a3f4a;
    --tagline-dark: #a7aebb;
    --tagline-light: #6b7280;
    --divider-dark: #4a4a4a;
    --divider-light: #c9ccd2;
  }
  * { box-sizing: border-box; margin: 0; padding: 0; }
  html, body {
    width: 1200px; height: 852px; overflow: hidden;
    background: var(--page-bg);
    font-family: "Open Sans", Arial, sans-serif;
  }
  .sheet {
    position: relative; width: 1200px; height: 852px;
    display: flex; flex-direction: column; align-items: center;
    justify-content: center; gap: 44px;
  }
  .card {
    position: relative; width: 620px; height: 354px;
    border-radius: 18px; overflow: hidden;
    box-shadow: 0 6px 18px rgba(0,0,0,.18);
  }
  .card--dark { background: linear-gradient(160deg, var(--card-dark-top), var(--card-dark-bottom)); }
  .card--light { background: var(--card-light); }
  .card__bands { position: absolute; inset: 0; width: 100%; height: 100%; }
  .card__name {
    position: absolute; top: 22px; right: 30px;
    color: #fff; font-weight: 700; font-size: 19px; letter-spacing: .2px;
  }
  .brand {
    position: absolute; left: 40px; top: 146px; width: 254px;
    display: flex; flex-direction: column; align-items: center;
  }
  .brand__dot {
    width: 60px; height: 60px; border-radius: 50%;
    background: radial-gradient(circle at 35% 30%, var(--navy-light), var(--navy) 55%, var(--navy-deep));
    margin-bottom: 10px;
  }
  .brand__name {
    font-weight: 800; font-size: 26px; letter-spacing: 1px; line-height: 1.2;
    text-transform: uppercase; white-space: nowrap;
  }
  .card--dark .brand__name { color: var(--navy-light); }
  .card--light .brand__name { color: var(--navy); }
  .brand__tagline {
    margin-top: 6px; font-size: 11.5px; font-weight: 600;
    letter-spacing: .6px; white-space: nowrap;
  }
  .card--dark .brand__tagline { color: var(--tagline-dark); }
  .card--light .brand__tagline { color: var(--tagline-light); }
  .card__divider {
    position: absolute; left: 318px; top: 156px; width: 1px; height: 150px;
  }
  .card--dark .card__divider { background: var(--divider-dark); }
  .card--light .card__divider { background: var(--divider-light); }
  .contact {
    position: absolute; left: 338px; top: 186px;
    list-style: none; display: flex; flex-direction: column; gap: 9px;
    font-size: 14px;
  }
  .card--dark .contact { color: var(--text-light); }
  .card--light .contact { color: var(--text-dark); }
  .contact__item { display: flex; align-items: center; gap: 9px; }
  .contact__icon { width: 14px; height: 14px; flex: none; }
</style>
</head>
<body>
<main class="sheet">

  <section class="card card--dark">
    <svg class="card__bands" viewBox="0 0 620 354" preserveAspectRatio="none" aria-hidden="true">
      <defs>
        <linearGradient id="bandDark" x1="0" y1="0" x2="1" y2="0">
          <stop offset="0" stop-color="#0b1640"/>
          <stop offset=".6" stop-color="#1d3a8f"/>
          <stop offset="1" stop-color="#2a4fb0"/>
        </linearGradient>
      </defs>
      <path d="M0 0H620V60C420 58 250 72 0 140Z" fill="url(#bandDark)"/>
      <path d="M0 140C250 72 420 58 620 60V70C420 70 250 86 0 154Z" fill="#8d96a3"/>
    </svg>
    <h1 class="card__name">Mira Castellan, MBA</h1>
    <div class="brand">
      <span class="brand__dot"></span>
      <span class="brand__name">Pillar Orchard</span>
      <span class="brand__tagline">Building Momentum for Success</span>
    </div>
    <span class="card__divider"></span>
    <ul class="contact">
      <li class="contact__item">
        <svg class="contact__icon" viewBox="0 0 16 16"><path d="M4 1l3 3-2 2c1 2 3 4 5 5l2-2 3 3-2 3C7 15 1 9 1 3z" fill="#3a63c7"/></svg>
        604-555-0182
      </li>
      <li class="contact__item">
        <svg class="contact__icon" viewBox="0 0 16 16"><rect x="1" y="3" width="14" height="10" rx="1" fill="#3a63c7"/><path d="M1 4l7 5 7-5" fill="none" stroke="#0b1640" stroke-width="1.3"/></svg>
        mira@pillarorchard.ca
      </li>
      <li class="contact__item">
        <svg class="contact__icon" viewBox="0 0 16 16"><circle cx="8" cy="8" r="7" fill="#3a63c7"/><path d="M1 8h14M8 1c3 3 3 11 0 14M8 1c-3 3-3 11 0 14" fill="none" stroke="#0b1640" stroke-width="1"/></svg>
        www.pillarorchard.ca
      </li>
    </ul>
  </section>

  <section class="card card--light">
    <svg class="card__bands" viewBox="0 0 620 354" preserveAspectRatio="none" aria-hidden="true">
      <defs>
        <linearGradient id="bandLight" x1="0" y1="0" x2="1" y2="0">
          <stop offset="0" stop-color="#0b1640"/>
          <stop offset=".6" stop-color="#1d3a8f"/>
          <stop offset="1" stop-color="#2a4fb0"/>
        </linearGradient>
      </defs>
      <path d="M0 0H620V60C420 58 250 72 0 140Z" fill="url(#bandLight)"/>
      <path d="M0 140C250 72 420 58 620 60V70C420 70 250 86 0 154Z" fill="#9aa3b0"/>
    </svg>
    <h1 class="card__name">Mira Castellan, MBA</h1>
    <div class="brand">
      <span class="brand__dot"></span>
      <span class="brand__name">Pillar Orchard</span>
      <span class="brand__tagline">Building Momentum for Success</span>
    </div>
    <span class="card__divider"></span>
    <ul class="contact">
      <li class="contact__item">
        <svg class="contact__icon" viewBox="0 0 16 16"><path d="M4 1l3 3-2 2c1 2 3 4 5 5l2-2 3 3-2 3C7 15 1 9 1 3z" fill="#1d3a8f"/></svg>
        604-555-0182
      </li>
      <li class="contact__item">
        <svg class="contact__icon" viewBox="0 0 16 16"><rect x="1" y="3" width="14" height="10" rx="1" fill="#1d3a8f"/><path d="M1 4l7 5 7-5" fill="none" stroke="#fff" stroke-width="1.3"/></svg>
        mira@pillarorchard.ca
      </li>
      <li class="contact__item">
        <svg class="contact__icon" viewBox="0 0 16 16"><circle cx="8" cy="8" r="7" fill="#1d3a8f"/><path d="M1 8h14M8 1c3 3 3 11 0 14M8 1c-3 3-3 11 0 14" fill="none" stroke="#fff" stroke-width="1"/></svg>
        www.pillarorchard.ca
      </li>
    </ul>
  </section>

</main>
</body>
</html>
```